Business Card Design Project

This design is a slimline business card 45mm x90mm, the card will be printed at 49mm x 94mm and cut to 45mm x90 mm, this needs to be considered in the design. The content required on the front and back of the business card is attached in a pdf; the design will be done using photo shop as we use CS6 in our business. The design needs to be developed using a CMYK colour pallet, the main colours used on our business are red, grey black and white. A snapshot of our business brochure and new website has been provided to give you an understanding on our businesses look and feel.
FRONT OF BUSINESS CARD
Director
Marcus Feld
Ph+61 0421780213
www.brightvanecontracting.com.au
marcusfeld@brightvanecontracting.com.au
BACK OF BUSINESS CARD
SUPPORTING CLIENTS IN
Oil & Gas I Minerals & Metals I Petrochemical I Manufacturing
Building & Construction I Telecommunication I Rail I Civil I New Industries
KNOWLEDGE I EXPERTISE I EXPERIENCE I CAPACITY

```html
<!DOCTYPE html>
<html lang="en">
<head>
<meta charset="utf-8">
<title>Brightvane Contracting – Business Card</title>
<link rel="stylesheet" href="https://fonts.googleapis.com/css2?family=Roboto:wght@400;700;900&display=swap">
<style>
  :root {
    --red: #e3202a;
    --red-dark: #c4141d;
    --black: #111111;
    --grey: #2b2b2b;
    --white: #ffffff;
    --page: #ffffff;
  }
  * { box-sizing: border-box; margin: 0; padding: 0; }
  html, body {
    width: 1200px; height: 1000px; overflow: hidden;
    background: var(--page);
    font-family: "Roboto", Arial, sans-serif;
    color: var(--black);
  }
  .card {
    position: absolute;
    left: 220px; width: 760px; height: 380px;
    background: var(--white);
    overflow: hidden;
    box-shadow: 6px 8px 14px rgba(0,0,0,0.35);
  }
  .card--front { top: 90px; }
  .card--back  { top: 570px; }

  /* Front */
  .brand {
    position: absolute; left: 70px; top: 44px;
    display: flex; align-items: center; gap: 16px;
    white-space: nowrap;
  }
  .brand__mark { width: 50px; height: 50px; background: var(--red); flex: none; }
  .brand__name {
    font-weight: 900; font-size: 40px; letter-spacing: 0.5px;
    color: var(--black); line-height: 1; text-transform: uppercase;
  }
  .tagline {
    position: absolute; left: 136px; top: 112px;
    font-weight: 700; font-size: 18px; color: var(--black);
    white-space: nowrap;
  }
  .contact { position: absolute; left: 54px; top: 160px; }
  .contact__role { font-size: 26px; line-height: 32px; }
  .contact__name { font-size: 26px; line-height: 34px; color: var(--red); }
  .contact__line { font-size: 19px; line-height: 28px; color: var(--grey); white-space: nowrap; }
  .contact__line--first { margin-top: 2px; }
  .front-scene {
    position: absolute; left: 0; right: 0; bottom: 0; height: 40px;
    background: linear-gradient(90deg, var(--red) 0%, var(--red) 40%, var(--red-dark) 100%);
  }
  .front-scene--rise {
    left: 440px; height: 190px;
    background: linear-gradient(180deg, var(--red) 0%, var(--red-dark) 100%);
    clip-path: polygon(0 100%, 8% 62%, 30% 45%, 55% 30%, 78% 22%, 100% 12%, 100% 100%);
  }

  /* Back */
  .sectors {
    position: absolute; left: 0; right: 0; top: 40px; text-align: center;
  }
  .sectors__title {
    font-weight: 700; font-size: 24px; color: var(--red); margin-bottom: 8px;
  }
  .sectors__line { font-size: 22px; line-height: 38px; color: var(--black); }
  .sep { color: var(--red); font-weight: 700; padding: 0 2px; }
  .back-scene {
    position: absolute; left: 0; right: 0; bottom: 0; height: 180px;
    background: linear-gradient(180deg, #2a2a2a 0%, var(--black) 45%);
    clip-path: polygon(0 35%, 15% 20%, 30% 8%, 48% 14%, 65% 4%, 82% 18%, 100% 10%, 100% 100%, 0 100%);
  }
  .values {
    position: absolute; left: 0; right: 0; bottom: 42px; text-align: center;
    color: var(--white); font-size: 22px; letter-spacing: 1.5px;
  }
  .values .dot { color: var(--red); padding: 0 6px; }
</style>
</head>
<body>
  <section class="card card--front" aria-label="Business card front">
    <div class="front-scene" role="img" aria-label="Red landscape silhouette"></div>
    <div class="front-scene front-scene--rise" role="img" aria-label="Red rising hills with an oil pump jack"></div>
    <div class="brand">
      <span class="brand__mark"></span>
      <span class="brand__name">Brightvane Contracting</span>
    </div>
    <p class="tagline">Providing Effective Project Controls and Management Solutions</p>
    <div class="contact">
      <p class="contact__role">Director</p>
      <p class="contact__name">Marcus Feld</p>
      <p class="contact__line contact__line--first">Ph+61 0497365128</p>
      <p class="contact__line">www.brightvanecontracting.com.au</p>
      <p class="contact__line">marcusfeld@brightvanecontracting.com.au</p>
    </div>
  </section>

  <section class="card card--back" aria-label="Business card back">
    <div class="sectors">
      <p class="sectors__title">SUPPORTING CLIENTS IN</p>
      <p class="sectors__line">Oil &amp; Gas <span class="sep">|</span> Minerals &amp; Metals <span class="sep">|</span> Petrochemical <span class="sep">|</span> Manufacturing</p>
      <p class="sectors__line">Building &amp; Construction <span class="sep">|</span> Telecommunication <span class="sep">|</span> Rail <span class="sep">|</span> Civil <span class="sep">|</span> New Industries</p>
    </div>
    <div class="back-scene" role="img" aria-label="Black hill silhouette with wind turbines"></div>
    <p class="values">KNOWLEDGE<span class="dot">.</span>EXPERTISE<span class="dot">.</span>EXPERIENCE<span class="dot">.</span>CAPACITY</p>
  </section>
</body>
</html>
```